This is book 2 to Mirage Harbor. I'm looking for something that feels similar, with the same cymatic image used on Antarctica on the first book cover (see the cover image attached; the original designer said this was the image used: https://www.filevaultexample.net/share/8k2m4p7q9r1t/cymatic-image.png). Differences: the cover should be all black (no Antarctica, no globe, nothing but the image), the cymatic image kind of a pale grayish white (subtle, not calling too much attention to itself. Think the subtle dragon on "The Boy beneath the Copper Lantern"--like that sort of). Same font as before, but red this time (with the color progression like in the first one, only red instead of blue), with the title (Mirage Assault), author name (M.J. Holt), and subtitle (Dawn of the Velorathi, Book 2)

Target Market(s)

adult action/adventure and thriller readers

Industry/Entity Type

media and literature

Colors
EB3D1F
EC4F4E
F09395
F8D3D4
FCEDEE

Requirements
Must have
• look like part of the series before
Should not have
• not too busy

```html
<!DOCTYPE html>
<html lang="en">
<head>
<meta charset="utf-8">
<title>Mirage Assault — Book Cover</title>
<link rel="stylesheet" href="https://fonts.googleapis.com/css2?family=Cinzel:wght@400;500&family=Oswald:wght@400&display=swap">
<style>
  :root {
    --page-bg: #dcdcdc;
    --cover-bg: #0f0f18;
    --red-bright: #e81c22;
    --red-deep: #7e1418;
    --red-glow: #ff3a3a;
    --subtitle-red: #ee2a2a;
    --author-white: #ffffff;
    --cymatic-light: #d8d8d8;
    --cymatic-mid: #6a6a70;
  }
  html, body {
    margin: 0;
    width: 1200px;
    height: 1200px;
    overflow: hidden;
    background: var(--page-bg);
  }
  .canvas {
    position: relative;
    width: 1200px;
    height: 1200px;
  }
  .cover {
    position: absolute;
    left: 217px;
    top: 26px;
    width: 766px;
    height: 1148px;
    background: var(--cover-bg);
    overflow: hidden;
  }
  .cover svg { display: block; }
  .title-text {
    font-family: "Oswald", "Arial Narrow", sans-serif;
    font-weight: 400;
    font-size: 232px;
  }
  .series-text {
    font-family: "Cinzel", "Times New Roman", serif;
    font-weight: 500;
    font-size: 31px;
    fill: var(--subtitle-red);
  }
  .author-text {
    font-family: "Cinzel", "Times New Roman", serif;
    font-weight: 500;
    font-size: 45px;
    fill: var(--author-white);
  }
</style>
</head>
<body>
<div class="canvas">
  <div class="cover">
    <svg width="766" height="1148" viewBox="0 0 766 1148" xmlns="http://www.w3.org/2000/svg">
      <defs>
        <radialGradient id="top-glow" cx="0.5" cy="0" r="0.6">
          <stop offset="0" stop-color="#a82a2e" stop-opacity="0.9"/>
          <stop offset="1" stop-color="#a82a2e" stop-opacity="0"/>
        </radialGradient>
        <linearGradient id="title-fill" x1="0" y1="0" x2="0" y2="1">
          <stop offset="0" stop-color="var(--red-deep)"/>
          <stop offset="0.45" stop-color="var(--red-bright)"/>
          <stop offset="1" stop-color="var(--red-deep)"/>
        </linearGradient>
        <linearGradient id="band-line" x1="0" y1="0" x2="1" y2="0">
          <stop offset="0" stop-color="var(--red-glow)" stop-opacity="0"/>
          <stop offset="0.5" stop-color="var(--red-glow)" stop-opacity="1"/>
          <stop offset="1" stop-color="var(--red-glow)" stop-opacity="0"/>
        </linearGradient>
        <linearGradient id="band-haze" x1="0" y1="0" x2="0" y2="1">
          <stop offset="0" stop-color="#5a0d10" stop-opacity="0"/>
          <stop offset="0.5" stop-color="#5a0d10" stop-opacity="0.7"/>
          <stop offset="1" stop-color="#5a0d10" stop-opacity="0"/>
        </linearGradient>
        <radialGradient id="cymatic-fill" cx="752" cy="962" r="440" gradientUnits="userSpaceOnUse">
          <stop offset="0" stop-color="var(--cymatic-mid)" stop-opacity="0.55"/>
          <stop offset="0.7" stop-color="var(--cymatic-light)" stop-opacity="0.45"/>
          <stop offset="1" stop-color="var(--cymatic-light)" stop-opacity="0.15"/>
        </radialGradient>
      </defs>

      <rect class="sky-glow" x="0" y="0" width="766" height="160" fill="url(#top-glow)"/>

      <circle class="cymatic-pattern" role="img" aria-label="Pale grey cymatic flower pattern radiating from the lower right corner" cx="752" cy="962" r="440" fill="url(#cymatic-fill)"/>

      <g class="title">
        <text class="title-text" x="64" y="245" textLength="627" lengthAdjust="spacingAndGlyphs" fill="url(#title-fill)">MIRAGE</text>
        <text class="title-text" x="40" y="437" textLength="675" lengthAdjust="spacingAndGlyphs" fill="url(#title-fill)">ASSAULT</text>
      </g>

      <g class="series-band">
        <rect x="0" y="455" width="766" height="95" fill="url(#band-haze)"/>
        <rect x="20" y="476" width="726" height="3" fill="url(#band-line)"/>
        <rect x="20" y="530" width="726" height="3" fill="url(#band-line)"/>
        <text class="series-text" x="383" y="519" text-anchor="middle" textLength="602" lengthAdjust="spacingAndGlyphs">DAWN OF THE VELORATHI, BOOK 2</text>
      </g>

      <text class="author-text" x="61" y="640" textLength="233" lengthAdjust="spacingAndGlyphs">M.J. HOLT</text>
    </svg>
  </div>
</div>
</body>
</html>
```